Letterhead Design Needed for Real Estate Office

We are a boutique real estate agency focused on property management. We need a letter head which is professional looking and include the following information:

Logo
ABN Number
Address
Postal Address
Phone
Fax
Mobile
Email
Website

Please note that the PLAVKTO logo can not be changed and must be positioned at the bottom right corner.

Please find attached the existing letterhead design for all the required elements.

Target Market(s)

Letterhead mostly used for service of notices, business letters, clients communication

Industry/Entity Type

Boutique

Colors

Designer to choose colors to be used in the design.

Requirements
Must have
• Logo

```html
<!DOCTYPE html>
<html lang="en">
<head>
<meta charset="utf-8">
<title>Meridian Partners Letterhead</title>
<link href="https://fonts.googleapis.com/css2?family=Exo+2:wght@400;600;700&display=swap" rel="stylesheet">
<style>
  :root {
    --brand-green: #a9c43b;
    --brand-ink: #3b3f3a;
    --text-dark: #1c1c1c;
    --soft-green: #eef3dc;
    --member-blue: #1f4c97;
    --edge-grey: #d6d6d6;
    --paper: #ffffff;
  }
  * { margin: 0; padding: 0; box-sizing: border-box; }
  html, body { width: 848px; height: 1200px; overflow: hidden; background: var(--paper); }
  .letterhead {
    position: relative;
    width: 848px;
    height: 1200px;
    background: var(--paper);
    border-left: 1px solid var(--edge-grey);
    font-family: "Exo 2", sans-serif;
    color: var(--text-dark);
    overflow: hidden;
  }
  .brand {
    position: absolute;
    left: 46px;
    top: 52px;
    display: flex;
    align-items: center;
    gap: 12px;
    color: var(--brand-ink);
    font-weight: 600;
    font-size: 24px;
    line-height: 1;
    white-space: nowrap;
  }
  .brand-square {
    width: 40px;
    height: 40px;
    background: var(--brand-green);
  }
  .contact {
    position: absolute;
    left: 340px;
    top: 22px;
    width: 490px;
    text-align: center;
    font-size: 14px;
    line-height: 19px;
    font-style: normal;
    white-space: nowrap;
  }
  .contact b { font-weight: 700; }
  .band { position: absolute; left: 0; width: 848px; }
  .band-top { top: 131px; height: 33px; }
  .band-bottom { top: 1142px; height: 40px; }
  .band path { fill: var(--brand-green); }
  .backdrop {
    position: absolute;
    left: 224px;
    top: 413px;
    width: 400px;
    height: 400px;
    border-radius: 50%;
    background: var(--soft-green);
  }
  .membership {
    position: absolute;
    left: 640px;
    top: 1100px;
    display: flex;
    align-items: center;
    gap: 10px;
    color: var(--member-blue);
    font-weight: 600;
    font-size: 28px;
    line-height: 1;
  }
  .membership-square {
    width: 26px;
    height: 26px;
    background: var(--member-blue);
  }
</style>
</head>
<body>
  <main class="letterhead">
    <header>
      <div class="brand">
        <span class="brand-square"></span>
        <span class="brand-name">Meridian Partners</span>
      </div>
      <address class="contact">
        ABN 48 210 775 302<br>
        Shop 12B 300-310 Harbour Street Lindfield NSW 2070 AUSTRALIA<br>
        PO BOX 415 Lindfield NSW 2070<br>
        <b>m</b> 0400 123 456 | <b>p</b> 9000 1234<br>
        <b>f</b> 9000 5678 | <b>e</b> hello@meridian.example | <b>w</b> http://meridian.example
      </address>
    </header>

    <svg class="band band-top" viewBox="0 0 848 33" aria-hidden="true">
      <path d="M0,0 H412 L426,13 H735 L749,0 H848 V33 H0 Z"/>
    </svg>

    <div class="backdrop" aria-hidden="true"></div>

    <div class="membership">
      <span class="membership-square"></span>
      <span>PLAVKTO</span>
    </div>

    <svg class="band band-bottom" viewBox="0 0 848 40" aria-hidden="true">
      <path d="M0,0 H584 L600,16 H848 V40 H0 Z"/>
    </svg>
  </main>
</body>
</html>
```